Web Design

I need a web design for our business please.

current web site www.fernwavedesk.com.au

i want the new design to look like: www.zavo.com

or www.calmerpaddle.com

Industry/Entity Type

Business

Font styles to use
Other font styles liked:
• Helvetica

Colors
33a6d7
ffffff
0792cd
f78f20
ec2027
9bcb3c

```html
<!DOCTYPE html>
<html lang="en">
<head>
<meta charset="utf-8">
<title>Home Energy Control</title>
<link rel="stylesheet" href="https://fonts.googleapis.com/css2?family=Lato:wght@300;400;700&family=Roboto:wght@500&display=swap">
<style>
  :root{
    --nav-bg:#0a6a98;
    --hero-top:#0f86c4;
    --hero-bottom:#0a93d6;
    --white:#ffffff;
    --ink:#444444;
    --muted:#9a9a9a;
    --body-text:#777777;
    --icon-ring:#3a9be2;
    --icon-core:#3b8dce;
    --app-tile:#3e4043;
    --app-border:#17a3e0;
  }
  *{margin:0;padding:0;box-sizing:border-box}
  html,body{width:1200px;height:1200px;overflow:hidden;background:var(--white)}
  body{position:relative;font-family:"Lato",sans-serif}

  .hero{position:absolute;left:0;top:0;width:1200px;height:595px;
    background:linear-gradient(180deg,var(--hero-top) 0%,#0c8ccc 55%,var(--hero-bottom) 100%)}
  .topbar{position:absolute;left:0;top:0;width:1200px;height:49px;background:var(--nav-bg)}
  .nav{position:absolute;top:0;height:49px;display:flex;align-items:center;
    font-family:"Roboto",sans-serif;font-weight:500;font-size:12.5px;color:var(--white);letter-spacing:.2px}
  .nav a{color:inherit;text-decoration:none;position:absolute;white-space:nowrap;transform:translateX(-50%)}
  .nav .download{border:1.5px solid var(--white);border-radius:14px;padding:6px 14px;transform:none}

  .device{position:absolute;left:154px;top:73px;width:221px;height:583px;border-radius:34px;
    background:linear-gradient(135deg,#f4f4f4 0%,#dcdcdc 100%);
    box-shadow:0 18px 40px rgba(0,0,0,.18)}

  .app-tile{position:absolute;left:484px;top:86px;width:157px;height:157px;border-radius:30px;
    background:var(--app-tile);border:6px solid var(--app-border)}

  .welcome{position:absolute;left:485px;top:262px;color:var(--white);font-size:55px;line-height:62px}
  .welcome .light{font-weight:300;letter-spacing:1px}
  .welcome .strong{font-weight:400;letter-spacing:-.5px}
  .intro{position:absolute;left:491px;top:405px;color:var(--white);font-weight:300;font-size:19px;line-height:29px}
  .intro .cta{margin-top:14px}

  .scroll-tab{position:absolute;left:576px;top:566px;width:44px;height:29px;background:var(--white)}
  .scroll-tab svg{position:absolute;left:13px;top:9px}

  .how{position:absolute;left:0;top:720px;width:1238px;text-align:center}
  .how h2{font-weight:400;font-size:40px;color:var(--ink);letter-spacing:-.5px}
  .how p{margin-top:10px;font-weight:300;font-size:19.5px;color:var(--muted)}

  .feature{position:absolute;top:871px;width:270px}
  .feature .badge{position:absolute;width:118px;height:118px;border-radius:50%;background:var(--icon-ring)}
  .feature .badge::after{content:"";position:absolute;inset:8px;border-radius:50%;background:var(--icon-core)}
  .feature .badge svg{position:absolute;left:29px;top:29px;z-index:1}
  .feature h3{position:absolute;top:151px;left:0;font-weight:400;font-size:21px;color:var(--ink);white-space:nowrap}
  .feature p{position:absolute;top:182px;left:0;font-weight:300;font-size:17px;line-height:28.5px;color:var(--body-text);width:270px}
</style>
</head>
<body>
  <section class="hero" role="img" aria-label="Blue-toned photo of a modern home interior"></section>

  <header class="topbar">
    <nav class="nav">
      <a style="left:626px">HOME</a>
      <a style="left:715px">ABOUT</a>
      <a style="left:813px">CONTACT</a>
      <a style="left:920px">SUPPORT</a>
      <a class="download" style="left:985px">DOWNLOAD</a>
    </nav>
  </header>

  <div class="device" role="img" aria-label="Smartphone showing the energy control app with coloured zone tiles"></div>

  <div class="app-tile" aria-hidden="true"></div>

  <h1 class="welcome">
    <span class="light">WELCOME&nbsp; TO</span><br>
    <span class="strong">HOME ENERGY CONTOL</span>
  </h1>

  <div class="intro">
    <p>The future is here and controlling your energy products<br>from the smart phone or tablet is just a click away.</p>
    <p class="cta">Contact our team for more info!</p>
  </div>

  <div class="scroll-tab">
    <svg width="18" height="12" viewBox="0 0 18 12"><path d="M2 2l7 7 7-7" fill="none" stroke="#0c5a55" stroke-width="3.2" stroke-linecap="round" stroke-linejoin="round"/></svg>
  </div>

  <section class="how">
    <h2>HOW IT WORKS</h2>
    <p>Ut enim ad minim veniam, quis nostrud exercitation ullamco.</p>
  </section>

  <article class="feature" style="left:163px">
    <div class="badge" style="left:70px">
      <svg width="60" height="60" viewBox="0 0 60 60"><path d="M26 6a4 4 0 0 1 8 0v31a9 9 0 1 1-8 0z" fill="none" stroke="#fff" stroke-width="3"/><circle cx="30" cy="45" r="5" fill="#fff"/><rect x="28.5" y="20" width="3" height="22" fill="#fff"/></svg>
    </div>
    <h3>Ut enim ad minim veniam</h3>
    <p>Lorem ipsum dolor sit amet, con-<br>sectetur&nbsp; isicing elit, sed do eius-<br>mod tempor incididunt ut labore<br>et dolore magna aliqua.</p>
  </article>

  <article class="feature" style="left:501px">
    <div class="badge" style="left:52px">
      <svg width="60" height="60" viewBox="0 0 60 60" fill="none" stroke="#fff" stroke-width="3.5"><path d="M3 16h54M3 30h54M3 44h54"/><rect x="16" y="11" width="9" height="10" fill="#3b8dce" stroke-width="3"/><rect x="33" y="25" width="9" height="10" fill="#3b8dce" stroke-width="3"/><rect x="16" y="39" width="9" height="10" fill="#3b8dce" stroke-width="3"/></svg>
    </div>
    <h3>Ut enim ad minim veniam</h3>
    <p>Lorem ipsum dolor sit amet, con-<br>sectetur&nbsp; isicing elit, sed do eius-<br>mod tempor incididunt ut labore<br>et dolore magna aliqua.</p>
  </article>

  <article class="feature" style="left:829px">
    <div class="badge" style="left:61px">
      <svg width="60" height="60" viewBox="0 0 60 60"><rect x="15" y="6" width="30" height="46" rx="3" fill="none" stroke="#fff" stroke-width="3"/><rect x="19" y="12" width="22" height="33" fill="#fff"/><circle cx="30" cy="48.5" r="1.6" fill="#fff"/></svg>
    </div>
    <h3>Ut enim ad minim veniam</h3>
    <p>Lorem ipsum dolor sit amet, con-<br>sectetur&nbsp; isicing elit, sed do eius-<br>mod tempor incididunt ut labore<br>et dolore magna aliqua.</p>
  </article>
</body>
</html>
```